KT-Systems advertising flag and billboard design

I need a design for advertising flag and a design for billboard.
Information can be obtained from https://kt-sytronik.de.
Updates
Target Market(s)
IT service for companies
Requirements
Must have
- Logo, contact information and services

```html
<!DOCTYPE html>
<html lang="de">
<head>
<meta charset="utf-8">
<title>KT-Systems – Billboard und Werbeflagge</title>
<link rel="stylesheet" href="https://fonts.googleapis.com/css2?family=Poppins:wght@300;400;600;700;800&display=swap">
<style>
  :root {
    --stage: #e6e6e8;
    --navy: #26234f;
    --navy-deep: #1d1b40;
    --accent-blue: #4a78e6;
    --wave-grey: #7c7d85;
    --photo-dark: #0f1a24;
    --photo-glow: #2c6f95;
    --cream: #f3e8d2;
    --white: #ffffff;
    --phone-blue: #2ea3e0;
  }
  * { box-sizing: border-box; margin: 0; padding: 0; }
  html, body { width: 1200px; height: 840px; overflow: hidden; }
  body {
    background: var(--stage);
    font-family: "Poppins", sans-serif;
    color: var(--white);
    position: relative;
  }

  /* Billboard */
  .billboard {
    position: absolute;
    left: 30px; top: 210px;
    width: 800px; height: 420px;
    background: var(--navy);
    overflow: hidden;
  }
  .billboard__art { position: absolute; inset: 0; }
  .billboard__content { position: absolute; left: 44px; top: 34px; width: 470px; }
  .brand-name {
    font-weight: 700;
    color: var(--white);
    letter-spacing: 0.04em;
    display: flex; align-items: center; gap: 10px;
  }
  .brand-name__dot { width: 12px; height: 12px; border-radius: 50%; background: var(--accent-blue); }
  .billboard .brand-name { font-size: 36px; }
  .billboard .headline {
    margin-top: 22px;
    font-size: 58px; font-weight: 700; line-height: 1.05;
  }
  .billboard .services {
    margin-top: 14px;
    font-size: 13px; font-weight: 400; line-height: 1.45;
    max-width: 460px;
  }
  .contact-line { display: flex; align-items: center; gap: 16px; margin-top: 20px; }
  .phone-icon { flex: none; }
  .billboard .phone-number { font-size: 40px; font-weight: 800; font-style: italic; color: var(--cream); }
  .billboard .web-address { margin: 4px 0 0 64px; font-size: 24px; font-weight: 300; letter-spacing: 0.03em; }

  /* Flag */
  .flag {
    position: absolute;
    left: 960px; top: 110px;
    width: 200px; height: 620px;
    background: var(--navy);
    border-radius: 190px 24px 0 0 / 240px 20px 0 0;
    overflow: hidden;
  }
  .flag__art { position: absolute; left: 0; top: 0; }
  .flag__content { position: absolute; left: 20px; top: 320px; right: 12px; }
  .flag .brand-name { font-size: 19px; gap: 7px; }
  .flag .brand-name__dot { width: 8px; height: 8px; }
  .flag .headline { margin-top: 34px; font-size: 31px; font-weight: 600; line-height: 1.12; }
  .flag .contact-line { gap: 6px; margin-top: 36px; }
  .flag .phone-number { font-size: 15px; font-weight: 800; font-style: italic; color: var(--cream); }
  .flag .web-address { margin: 2px 0 0 20px; font-size: 13px; font-weight: 300; }

  .ring { position: absolute; border: 3px solid var(--wave-grey); border-radius: 50%; }
</style>
</head>
<body>

<section class="billboard" aria-label="Billboard KT-Systems">
  <svg class="billboard__art" width="800" height="420" viewBox="0 0 800 420">
    <defs>
      <radialGradient id="billboard-photo" cx="0.45" cy="0.45" r="0.7">
        <stop offset="0" stop-color="var(--photo-glow)"/>
        <stop offset="0.55" stop-color="#16303f"/>
        <stop offset="1" stop-color="var(--photo-dark)"/>
      </radialGradient>
    </defs>
    <path d="M600 0 C560 60 515 130 540 210 C565 290 560 360 520 420 L800 420 L800 0 Z" fill="var(--wave-grey)"/>
    <path d="M650 0 C600 70 600 130 630 200 C660 270 640 350 630 420 L800 420 L800 0 Z"
          fill="url(#billboard-photo)" role="img" aria-label="Foto: Hände mit Smartphone, darüber ein leuchtendes Sicherheitsschild mit Schloss"/>
    <path d="M640 0 C600 80 555 140 575 215 C600 300 560 370 505 420"
          fill="none" stroke="var(--accent-blue)" stroke-width="9"/>
  </svg>
  <span class="ring" style="left:540px; top:150px; width:30px; height:30px;"></span>
  <span class="ring" style="left:500px; top:370px; width:20px; height:20px;"></span>

  <div class="billboard__content">
    <div class="brand-name"><span class="brand-name__dot"></span>KT-Systems</div>
    <h1 class="headline">Ihr Partner<br>für IT-Service</h1>
    <p class="services">Unsere Expertise erstreckt sich über die Lösung von Hardware- und Softwareproblemen, sodass Sie sich auf reibungslose Abläufe in Ihrer IT-Umgebung verlassen können.</p>
    <div class="contact-line">
      <svg class="phone-icon" width="48" height="48" viewBox="0 0 48 48" aria-hidden="true">
        <circle cx="24" cy="24" r="24" fill="var(--phone-blue)"/>
        <path d="M17 13c1.5-1 3-.6 3.8.8l2 3.6c.7 1.3.3 2.6-.9 3.4l-1.4.9c1 2.6 3.2 4.8 5.8 5.8l.9-1.4c.8-1.2 2.1-1.6 3.4-.9l3.6 2c1.4.8 1.8 2.3.8 3.8l-1 1.5c-1 1.5-3 2.1-4.8 1.4C22.5 32 16 25.5 13.1 18.8c-.7-1.8-.1-3.8 1.4-4.8z" fill="var(--navy)"/>
      </svg>
      <span class="phone-number">01234-5678901</span>
    </div>
    <p class="web-address">kt-sytronik.com</p>
  </div>
</section>

<section class="flag" aria-label="Werbeflagge KT-Systems">
  <svg class="flag__art" width="200" height="300" viewBox="0 0 200 300">
    <defs>
      <radialGradient id="flag-photo" cx="0.35" cy="0.45" r="0.8">
        <stop offset="0" stop-color="var(--photo-glow)"/>
        <stop offset="0.5" stop-color="#18303e"/>
        <stop offset="1" stop-color="var(--photo-dark)"/>
      </radialGradient>
    </defs>
    <path d="M0 0 L200 0 L200 250 C170 200 120 230 90 230 C50 230 20 220 0 205 Z"
          fill="url(#flag-photo)" role="img" aria-label="Foto: Hand mit Smartphone und leuchtendem Sicherheitsschild mit Schloss"/>
    <path d="M0 215 C40 240 80 260 120 250 C155 242 180 245 200 262 L200 250 C180 230 150 228 120 238 C80 250 40 230 0 205 Z"
          fill="var(--accent-blue)"/>
  </svg>
  <span class="ring" style="left:96px; top:276px; width:22px; height:22px;"></span>

  <div class="flag__content">
    <div class="brand-name"><span class="brand-name__dot"></span>KT-Systems</div>
    <h2 class="headline">Ihr<br>Partner<br>für<br>IT-Service</h2>
    <div class="contact-line">
      <svg class="phone-icon" width="14" height="14" viewBox="0 0 48 48" aria-hidden="true">
        <circle cx="24" cy="24" r="24" fill="var(--phone-blue)"/>
        <path d="M17 13c1.5-1 3-.6 3.8.8l2 3.6c.7 1.3.3 2.6-.9 3.4l-1.4.9c1 2.6 3.2 4.8 5.8 5.8l.9-1.4c.8-1.2 2.1-1.6 3.4-.9l3.6 2c1.4.8 1.8 2.3.8 3.8l-1 1.5c-1 1.5-3 2.1-4.8 1.4C22.5 32 16 25.5 13.1 18.8c-.7-1.8-.1-3.8 1.4-4.8z" fill="var(--navy)"/>
      </svg>
      <span class="phone-number">01234-5678901</span>
    </div>
    <p class="web-address">kt-sytronik.com</p>
  </div>
</section>

</body>
</html>
```